WeatheredIt.net wordpress design

Concept: Website where personal stories, personal videos can be posted as a challenge while awaiting the wisdom of experience from others who have Weathered it same event or challenge in their lifetime.
Support aspects will be in 4 quadrants of Challenges:
1. Financial 2. Medical & Physical
3. Legal Matters 4. Psychological & Spiritual - ability to chat online with a spiritual/psychological counselor or life coach
Updates
Project Deadline Extended
Reason: Bit more time to complete designs.
Wanted to thank all of you for your designs! Greatly appreciated. Very creative ideas that captured the essence of this website. Will be back with a selection very shortly.
Target Market(s)
Anyone looking for a solution based upon experiential wisdom
Industry/Entity Type
Financial
Requirements
Must have
- Interactive website: Where you can post a challenge or issue via a written question or a video and ask for a solution.
Ability to access any of the 4 Quadrants (as listed above) to ask for an expert, via experience, advice and wisdom from those who have similar challenges.

```html
<!DOCTYPE html>
<html lang="en">
<head>
<meta charset="utf-8">
<title>WeatheredIt.net</title>
<link rel="stylesheet" href="https://fonts.googleapis.com/css2?family=Asap+Condensed:wght@500;600;700&display=swap">
<style>
  :root {
    --band-top: #d6d6c4;
    --band-form: #cfcfb8;
    --band-categories: #c6c4a7;
    --band-footer: #bcb898;
    --brown: #3a2914;
    --mustard: #c8ab00;
    --cream: #f3efe0;
  }
  * { box-sizing: border-box; margin: 0; padding: 0; }
  html, body { width: 853px; height: 1200px; overflow: hidden; }
  body { font-family: "Asap Condensed", "Arial Narrow", sans-serif; color: var(--brown); }
  .page { position: relative; width: 853px; height: 1200px; background: var(--band-form); }

  .masthead { position: absolute; left: 0; top: 0; width: 853px; height: 124px; background: var(--band-top); }
  .site-title {
    position: absolute; right: 20px; top: 4px;
    font-size: 94px; font-weight: 700; letter-spacing: -1px; line-height: 1.1;
    text-shadow: -2px -2px 0 var(--mustard);
  }

  .share { position: absolute; left: 0; top: 124px; width: 853px; height: 496px; }
  .section-heading { position: absolute; left: 0; width: 853px; text-align: center; font-weight: 700; }
  .share .section-heading { top: 43px; font-size: 55px; }

  .field {
    position: absolute; left: 77px; width: 696px; background: var(--mustard);
    font-size: 36px; font-weight: 700; padding: 0 10px; line-height: 50px;
  }
  .field-name { top: 139px; height: 50px; }
  .field-email { top: 197px; height: 51px; }
  .field-video { top: 256px; height: 51px; }
  .field-question { top: 315px; height: 90px; }

  .btn {
    position: absolute; background: var(--brown); color: var(--cream);
    font-weight: 600; text-align: center; border-radius: 3px;
  }
  .btn-browse { right: 14px; top: 9px; width: 87px; height: 32px; line-height: 32px; font-size: 19px; }
  .btn-submit { left: 633px; top: 413px; width: 140px; height: 46px; line-height: 46px; font-size: 27px; }

  .categories { position: absolute; left: 0; top: 620px; width: 853px; height: 393px; background: var(--band-categories); }
  .categories .section-heading { top: 24px; font-size: 58px; }
  .category {
    position: absolute; width: 297px; height: 100px; background: var(--brown); color: var(--cream);
    display: flex; align-items: center; justify-content: center; border-radius: 2px; font-weight: 600;
  }
  .cat-financial { left: 123px; top: 123px; font-size: 50px; }
  .cat-medical { left: 447px; top: 123px; font-size: 34px; }
  .cat-psych { left: 123px; top: 245px; font-size: 26px; }
  .cat-legal { left: 447px; top: 245px; font-size: 50px; }

  .site-footer { position: absolute; left: 0; top: 1013px; width: 853px; height: 187px; background: var(--band-footer); }
  .footer-brand { position: absolute; left: 0; top: 34px; width: 853px; display: flex; flex-direction: column; align-items: center; }
  .brand-square { width: 80px; height: 80px; background: var(--mustard); }
  .brand-name { margin-top: 8px; font-size: 24px; font-weight: 700; letter-spacing: 1px; }
</style>
</head>
<body>
<div class="page">
  <header class="masthead">
    <h1 class="site-title">Weathered it</h1>
  </header>

  <section class="share">
    <h2 class="section-heading">Share an experience of your own</h2>
    <div class="field field-name">Name</div>
    <div class="field field-email">Email</div>
    <div class="field field-video">Video<span class="btn btn-browse">Browse</span></div>
    <div class="field field-question">Question</div>
    <div class="btn btn-submit">Submit</div>
  </section>

  <section class="categories">
    <h2 class="section-heading">Browse by categories</h2>
    <div class="category cat-financial">Financial</div>
    <div class="category cat-medical">Medical &amp; Physical</div>
    <div class="category cat-psych">Psychological &amp; Spiritual</div>
    <div class="category cat-legal">Legal</div>
  </section>

  <footer class="site-footer">
    <div class="footer-brand">
      <span class="brand-square"></span>
      <span class="brand-name">WEATHERED IT</span>
    </div>
  </footer>
</div>
</body>
</html>
```